Start-up braucht modernes/hochwertiges Getränkeetikett
Zielgruppe
Wir sind ein modernes, nachhaltiges Start-up, welches eine neue Getränkekategorie auf den Markt bringt. Ein sogenanntes Elektrolyt-Getränk mit dem Namen KLORV5. Es ist abgefüllt in eine 500 ml Flasche und enthält Magnesium, Kalzium, Kalium, und Natrium. Diese Stoffe (Elektrolyte) dienen der körperlichen Hydrierung. Zu Dehydrierung kann es durch Hitze, Alkohol, Sport oder Krankheit kommen. Krankheit liegt bei uns allerdings nicht im Fokus. In unserer Zielgruppe befinden sich hauptsächlich Personen im Alter von 18 - 29 Jahren.
Die Geschmacksrichtung ist Zitrone-Limette.
Aufgabenstellung
Das Etikett soll:
- MODERN, SCHLICHT und HOCHWERTIG sein, so dass es im Supermarkt hervorsticht
- erkenntlich machen, dass die Stoffe Magnesium, Natrium, Kalzium und Kalium enthalten sind
- sich farblich deutlich von der Farbe des Inhalts (weiß) abheben. (Vorzugsweise mit einem hellen Blau, türkis)
- für unsere junge Zielgruppe ansprechend sein
- ebenfalls auf die Geschmacksrichtung (Zitrone-Limette) hinweisen, und zwar so, dass wenn man eine weitere Geschmacksrichtung auf den Markt bringen möchte, diese leicht angepasst werden kann.
- nicht nach einem Energydrink oder einem typischen Sportgetränk aussehen
- unter dem Namen den Slogan 'Elektrolyt-Getränk' stehen haben
-Das Etikett ist nicht dursichtig sondern besteht aus Papier
Der Name sowie das Logo können selbstverständlich farblich verändert werden. Bei dem Logo können auch größere Änderungen vollzogen werden.
Bitte beachten Sie die unten zu stehenden Regler um sich einen guten Überblick über unsere Vorstellungen zu verschaffen. Die Platzierung des EAN-Code ist für ihr Design irrelevat .
Bei Unklarheiten gerne nachfragen!

```html
<!DOCTYPE html>
<html lang="de">
<head>
<meta charset="utf-8">
<title>KLORV5 Etikett</title>
<link href="https://fonts.googleapis.com/css2?family=Lexend:wght@200;600&family=Montserrat:wght@700;800&display=swap" rel="stylesheet">
<style>
  :root {
    --strip-top: #a7cfe6;
    --strip-mid: #b5c8e6;
    --strip-bottom: #c9ecea;
    --lemon: #e6e07f;
    --lime: #97c48a;
    --cyan-light: #a9eef6;
    --cyan: #0fc0d8;
    --royal: #3f70b8;
    --sky-soft: #93bedb;
    --teal: #4dcfae;
    --mint: #b5f1df;
    --white: #ffffff;
  }
  * { margin: 0; padding: 0; box-sizing: border-box; }
  html, body { width: 667px; height: 1200px; overflow: hidden; background: #ffffff; }

  .label {
    position: relative;
    width: 667px;
    height: 1200px;
    overflow: hidden;
    background: linear-gradient(180deg, var(--cyan-light) 0%, var(--cyan) 18%, var(--royal) 48%, var(--teal) 82%, var(--mint) 100%);
  }
  .label__field {
    position: absolute; inset: 0 0 0 174px;
    background:
      radial-gradient(ellipse 260px 380px at 100% 30%, rgba(147,190,219,0.85), transparent 70%),
      radial-gradient(ellipse 300px 260px at 0% 18%, rgba(169,238,246,0.7), transparent 70%),
      radial-gradient(ellipse 260px 300px at 0% 52%, rgba(160,190,235,0.75), transparent 70%),
      radial-gradient(ellipse 280px 260px at 100% 88%, rgba(160,220,210,0.8), transparent 70%),
      radial-gradient(ellipse 260px 200px at 20% 100%, rgba(181,241,223,0.9), transparent 70%),
      linear-gradient(180deg, var(--cyan-light) 0%, var(--cyan) 16%, #2f9fcf 32%, var(--royal) 50%, #4a8fb8 66%, var(--teal) 84%, var(--mint) 100%);
  }
  .label__strip {
    position: absolute; top: 0; bottom: 0; left: 0; width: 95px;
    background: linear-gradient(180deg, var(--strip-top) 0%, var(--strip-mid) 50%, var(--strip-bottom) 100%);
  }
  .flavour-band { position: absolute; top: 0; bottom: 0; }
  .flavour-band--lemon { left: 95px; width: 37px; background: var(--lemon); }
  .flavour-band--lime { left: 132px; width: 42px; background: var(--lime); }

  .upright {
    position: absolute;
    transform: rotate(-90deg);
    transform-origin: top left;
    white-space: nowrap;
  }
  .flavour-name {
    font-family: "Montserrat", sans-serif;
    font-weight: 800;
    font-size: 17px;
    line-height: 20px;
    letter-spacing: 0.5px;
  }
  .flavour-name--lemon { left: 111px; top: 184px; color: #8cc98a; }
  .flavour-name--lime { left: 136px; top: 184px; color: #ece08a; }

  .brand-name {
    left: 176px; top: 902px;
    font-family: "Lexend", sans-serif;
    font-weight: 600;
    font-size: 198px;
    line-height: 1;
    letter-spacing: 2px;
    color: var(--white);
  }
  .brand-badge { position: absolute; left: 198px; top: 950px; }

  .tagline {
    left: 368px; top: 527px;
    font-family: "Lexend", sans-serif;
    font-weight: 200;
    font-size: 41px;
    line-height: 44px;
    color: var(--white);
  }
  .minerals {
    left: 428px; top: 527px;
    list-style: none;
    font-family: "Montserrat", sans-serif;
    font-weight: 700;
    font-size: 17px;
    line-height: 36px;
    color: var(--white);
  }
</style>
</head>
<body>
  <main class="label">
    <div class="label__field"></div>
    <div class="label__strip"></div>
    <div class="flavour-band flavour-band--lemon"></div>
    <div class="flavour-band flavour-band--lime"></div>

    <span class="upright flavour-name flavour-name--lemon">ZITRONE</span>
    <span class="upright flavour-name flavour-name--lime">LIMETTE</span>

    <h1 class="upright brand-name">KLORV5</h1>
    <svg class="brand-badge" width="156" height="156" viewBox="0 0 156 156" aria-hidden="true">
      <circle cx="78" cy="78" r="74" fill="none" stroke="#ffffff" stroke-width="2.5"/>
    </svg>

    <p class="upright tagline">Elektrolyt-Getränk</p>
    <ul class="upright minerals">
      <li>Magnesium</li>
      <li>Natrium</li>
      <li>Kalcium</li>
      <li>Kalium</li>
    </ul>
  </main>
</body>
</html>
```